Private Learning Centre in Singapore needs a flyer design

We need a flyer design for our upcoming education fair and also able to use it for day to day purpose. The aim is to attract parents, students to enrol for classes by offering them free trial class/assessment. 2 sided flyer with the front page as the logo only and details on the other page. We would like to see a final design in blue, white and it should be curious and attractive enough not to allow customers to throw it away once they received it.

Education

```html
<!DOCTYPE html>
<html lang="en">
<head>
<meta charset="utf-8">
<title>Bright Path Academy – Flyer</title>
<link rel="stylesheet" href="https://fonts.googleapis.com/css2?family=Open+Sans:wght@400;600;700&display=swap">
<style>
  :root {
    --page-bg: #e9e6e1;
    --navy: #132a5c;
    --navy-deep: #0f2350;
    --band-blue: #0f3f84;
    --text-blue: #3949a6;
    --paper: #f2f2f3;
    --white: #ffffff;
    --faint: #e3e4e8;
    --photo-top: #7a8a74;
    --photo-mid: #b8a48c;
    --photo-low: #8fa06a;
  }
  * { margin: 0; padding: 0; box-sizing: border-box; }
  html, body { width: 1200px; height: 947px; overflow: hidden; }
  body {
    background: var(--page-bg);
    font-family: "Open Sans", sans-serif;
    position: relative;
  }
  .flyer {
    position: absolute;
    top: 115px;
    width: 505px;
    height: 716px;
    box-shadow: 0 6px 18px rgba(0,0,0,0.25);
    overflow: hidden;
  }
  /* Front side */
  .flyer-front {
    left: 60px;
    background: linear-gradient(90deg, var(--navy) 0%, #0d2d64 55%, var(--navy) 100%);
    display: flex;
    flex-direction: column;
    align-items: center;
    justify-content: center;
    gap: 26px;
  }
  .front-mark {
    width: 120px;
    height: 120px;
    border-radius: 50%;
    background: var(--paper);
  }
  .front-name {
    color: var(--white);
    font-weight: 600;
    font-size: 34px;
    letter-spacing: 1px;
    text-align: center;
    line-height: 1.2;
  }
  /* Back side */
  .flyer-back {
    left: 635px;
    background: var(--paper);
  }
  .hero-photo {
    position: absolute;
    left: 0; top: 0;
    width: 100%; height: 170px;
    background: linear-gradient(180deg, var(--photo-top) 0%, var(--photo-mid) 50%, var(--photo-low) 100%);
  }
  .social-tag {
    position: absolute;
    right: 18px; top: 18px;
    color: var(--white);
    font-size: 13px;
    font-weight: 600;
    display: flex;
    align-items: center;
    gap: 6px;
  }
  .social-tag::before {
    content: "";
    width: 14px; height: 14px;
    background: var(--white);
  }
  .title-band {
    position: absolute;
    left: 0; top: 170px;
    width: 100%; height: 80px;
    background: var(--band-blue);
  }
  .band-title {
    position: absolute;
    left: 190px; top: 12px;
    color: var(--white);
    font-size: 40px;
    font-weight: 400;
  }
  .badge {
    position: absolute;
    left: 44px; top: 150px;
    width: 120px; height: 120px;
    border-radius: 50%;
    background: var(--white);
    display: flex;
    align-items: center;
    justify-content: center;
    text-align: center;
    color: var(--text-blue);
    font-size: 15px;
    font-weight: 600;
    line-height: 1.25;
    padding: 0 16px;
  }
  .faint-circle {
    position: absolute;
    left: 112px; top: 380px;
    width: 280px; height: 280px;
    border-radius: 50%;
    background: var(--faint);
    opacity: 0.6;
  }
  .body-copy {
    position: absolute;
    left: 20px; right: 20px; top: 302px;
    color: var(--text-blue);
    font-size: 16.5px;
    line-height: 1.38;
    text-align: center;
  }
  .body-copy p + p { margin-top: 40px; }
  .body-copy strong { font-weight: 600; }
  .contact-block {
    position: absolute;
    left: 0; right: 0; top: 590px;
    text-align: center;
    color: var(--text-blue);
    font-weight: 700;
  }
  .contact-name {
    display: inline-block;
    font-size: 19px;
    padding: 0 6px 3px;
    border-bottom: 1px solid var(--text-blue);
  }
  .contact-phone {
    margin-top: 4px;
    font-size: 21px;
    display: flex;
    align-items: center;
    justify-content: center;
    gap: 6px;
  }
  .footer-bar {
    position: absolute;
    left: 0; bottom: 0;
    width: 100%; height: 56px;
    background: var(--navy-deep);
    color: var(--white);
    font-size: 12.5px;
    display: flex;
    align-items: center;
  }
  .footer-bar::before {
    content: "";
    position: absolute;
    left: 50%; top: -8px;
    transform: translateX(-50%);
    border-left: 10px solid transparent;
    border-right: 10px solid transparent;
    border-bottom: 8px solid var(--navy-deep);
  }
  .footer-item { flex: 1; text-align: center; }
  .footer-item + .footer-item { border-left: 1px solid rgba(255,255,255,0.3); }
  .footer-item b { font-weight: 700; }
</style>
</head>
<body>
  <section class="flyer flyer-front">
    <div class="front-mark"></div>
    <div class="front-name">Bright Path Academy</div>
  </section>

  <section class="flyer flyer-back">
    <div class="hero-photo" role="img" aria-label="Photo of four smiling teenage students outdoors"></div>
    <div class="social-tag">Linkup</div>
    <div class="title-band">
      <h1 class="band-title">Free Trial Class</h1>
    </div>
    <div class="badge">Bright Path Academy</div>
    <div class="faint-circle"></div>
    <div class="body-copy">
      <p><strong>Bright Path Academy</strong> is where you can develop academic and life skills. Our teachers are the heartbeat of the business. They inspire and nurture students, helping them surpass their expectations.</p>
      <p>We cover English, Mathematics and Science from Primary and Secondary Levels.</p>
    </div>
    <div class="contact-block">
      <div class="contact-name">Bright Path Academy</div>
      <div class="contact-phone">
        <svg width="22" height="20" viewBox="0 0 22 20" aria-hidden="true">
          <path d="M2 7 Q11 0 20 7 L18 10 L15 8 L15 6 Q11 4.5 7 6 L7 8 L4 10 Z" fill="#3949a6"/>
          <rect x="4" y="11" width="14" height="8" rx="2" fill="#3949a6"/>
          <circle cx="11" cy="15" r="2.2" fill="#f2f2f3"/>
        </svg>
        <span>6100 2475</span>
      </div>
    </div>
    <footer class="footer-bar">
      <div class="footer-item"><b>e:</b> enquire@brightpathacademy.com</div>
      <div class="footer-item"><b>a:</b> 48 Seaview Lane S428910</div>
    </footer>
  </section>
</body>
</html>
```